Beauty Salon Design

The business card design will be for a new beauty salon opening up.

The therapist has over 11 years at a leading beauty Salon in perth.

The two colours that the salon will use is black and gold.

Industry/Entity Type

Beauty Salon

Contact Information for Business Card

Velmora Beauty

Corinne Ashdale
Advanced beauty therapist
0457 318 042

Monday - Friday 9am - 2.30pm
Weekends and nights by appointment only

Waxing, Tinting, Swedish massage, hot stone massage, facials, peels, micro, LED light treatment, skin needling and retail products.

```html
<!DOCTYPE html>
<html lang="en">
<head>
<meta charset="utf-8">
<title>Velmora Beauty – Business Card</title>
<link rel="stylesheet" href="https://fonts.googleapis.com/css2?family=Libre+Baskerville:wght@400;700&family=Alegreya+Sans:ital,wght@1,700;1,800&display=swap">
<style>
  :root {
    --stage: #8e8e90;
    --ink: #1f1c1d;
    --charcoal: #2a2728;
    --slate: #8a898c;
    --gold: #d4c61c;
    --gold-deep: #a3952e;
    --gold-light: #d8cc6a;
    --bronze: #6f5442;
    --bronze-light: #9a8170;
    --white: #ffffff;
  }
  * { box-sizing: border-box; margin: 0; padding: 0; }
  html, body { width: 1200px; height: 900px; overflow: hidden; }
  body {
    background: var(--stage);
    position: relative;
    font-family: "Libre Baskerville", Georgia, serif;
  }
  .card {
    position: absolute;
    left: 290px;
    width: 620px;
    height: 354px;
    overflow: hidden;
    box-shadow: 0 10px 28px rgba(0,0,0,0.35);
  }
  .card--back { top: 68px; background: var(--gold-deep); }
  .card--front { top: 478px; background: var(--charcoal); }
  .card__art { position: absolute; inset: 0; width: 620px; height: 354px; }

  /* back side */
  .hours { position: absolute; left: 28px; top: 18px; color: var(--gold); font-family: "Alegreya Sans", Arial, sans-serif; font-style: italic; }
  .hours__days { font-size: 23px; font-weight: 800; letter-spacing: 0.3px; }
  .hours__note { font-size: 13px; font-weight: 700; margin-top: 1px; }
  .services {
    position: absolute;
    left: 36px; top: 118px;
    list-style: none;
    color: var(--ink);
    font-weight: 700;
    font-size: 18px;
    line-height: 1.4;
  }

  /* front side */
  .brand-name {
    position: absolute;
    left: 34px; top: 36px;
    color: var(--white);
    font-size: 29px;
    font-weight: 700;
  }
  .contact {
    position: absolute;
    left: 60px; top: 218px;
    color: var(--white);
    font-family: "Alegreya Sans", Arial, sans-serif;
    font-style: italic;
    font-weight: 800;
  }
  .contact__name { font-size: 31px; line-height: 1.15; }
  .contact__role { font-size: 23px; line-height: 1.25; font-weight: 700; }
  .contact__phone { font-size: 23px; line-height: 1.3; font-weight: 700; }
</style>
</head>
<body>

  <section class="card card--back" aria-label="Business card, back">
    <svg class="card__art" viewBox="0 0 620 354" aria-hidden="true">
      <defs>
        <linearGradient id="back-photo-tone" x1="0" y1="0" x2="1" y2="0">
          <stop offset="0" stop-color="#a3952e" stop-opacity="0"/>
          <stop offset="0.35" stop-color="#b9ab4a"/>
          <stop offset="0.75" stop-color="#d8cc6a"/>
          <stop offset="1" stop-color="#b3a543"/>
        </linearGradient>
      </defs>
      <rect width="620" height="354" fill="var(--gold-deep)"/>
      <path role="img" aria-label="Gold-toned beauty portrait photograph" d="M300 48 C430 30 530 24 620 22 V300 C520 300 400 300 300 290 Z" fill="url(#back-photo-tone)"/>
      <path d="M0 0 H620 V22 C480 30 330 60 0 110 Z" fill="var(--ink)"/>
      <path d="M0 110 C330 60 480 30 620 22" fill="none" stroke="var(--white)" stroke-width="2"/>
    </svg>
    <div class="hours">
      <p class="hours__days">Monday - Friday 9am - 2.30pm</p>
      <p class="hours__note">Weekends and nights by appointment only</p>
    </div>
    <ul class="services">
      <li>Waxing, Tinting,</li>
      <li>Swedish massage,</li>
      <li>Hot stone massage,</li>
      <li>Facials, Peels,</li>
      <li>Micro, LED light treatment,</li>
      <li>Skin needling &amp; Retail products.</li>
    </ul>
  </section>

  <section class="card card--front" aria-label="Business card, front">
    <svg class="card__art" viewBox="0 0 620 354" aria-hidden="true">
      <defs>
        <linearGradient id="front-base" x1="0" y1="0" x2="1" y2="1">
          <stop offset="0" stop-color="#242122"/>
          <stop offset="0.55" stop-color="#3a3536"/>
          <stop offset="1" stop-color="#2a2728"/>
        </linearGradient>
        <linearGradient id="front-grey-band" x1="0" y1="0" x2="1" y2="1">
          <stop offset="0" stop-color="#5e5c5f"/>
          <stop offset="1" stop-color="#9a999c"/>
        </linearGradient>
        <radialGradient id="front-photo-tone" cx="0.42" cy="0.45" r="0.62">
          <stop offset="0" stop-color="#9a8170"/>
          <stop offset="0.45" stop-color="#6f5442"/>
          <stop offset="1" stop-color="#2a2728" stop-opacity="0"/>
        </radialGradient>
        <linearGradient id="front-gold-tone" x1="0" y1="0" x2="0" y2="1">
          <stop offset="0" stop-color="#d4c61c" stop-opacity="0.9"/>
          <stop offset="0.5" stop-color="#c9bb22"/>
          <stop offset="1" stop-color="#d4c61c" stop-opacity="0.85"/>
        </linearGradient>
      </defs>
      <rect width="620" height="354" fill="url(#front-base)"/>
      <path d="M300 0 H430 C470 120 540 250 620 300 V354 H340 C360 250 340 120 300 0 Z" fill="url(#front-grey-band)" opacity="0.85"/>
      <rect role="img" aria-label="Close-up beauty portrait photograph with bronze make-up" x="0" y="0" width="470" height="354" fill="url(#front-photo-tone)"/>
      <path role="img" aria-label="Gold flourish ornament" d="M395 20 C440 40 470 90 480 150 C490 210 470 270 440 354 H560 C600 300 610 240 600 180 C590 120 540 60 470 30 C445 18 420 14 395 20 Z" fill="url(#front-gold-tone)"/>
    </svg>
    <h1 class="brand-name">Velmora Beauty</h1>
    <div class="contact">
      <p class="contact__name">Corinne Ashdale</p>
      <p class="contact__role">Advanced beauty therapist</p>
      <p class="contact__phone">T: 0457 318 042</p>
    </div>
  </section>

</body>
</html>
```